Dentist Ad for Airline Magazine

A full page print ad for magazine. Details below.

Target Market(s)

Mine workers and rural patients who fly in and out of the main city.

Industry/Entity Type

Airline

Requirements
Must have
• Copywriting as per attachment. Magazine print specifications as per attachment. Inviting colours (blue shades, perhaps some green/yellow). Comforting look and picture. Professional feel. Picture can be of a smiling or sleeping relaxed person (see business websites http://www.calmharbordentalcare.com and http://www.willowbankdentalclinic.com.au) - as we bring patients with complex dental problems or fear of the dentist, back to health whilst they enjoy a relaxing sleep (sedation).
Nice to have
• - stylised image of an aeroplane route across the text or at the footer

```html
<!DOCTYPE html>
<html lang="en">
<head>
<meta charset="utf-8">
<title>Fly-in Fly-out Dental Transformations – Magazine Ad</title>
<link rel="stylesheet" href="https://fonts.googleapis.com/css2?family=Nunito:wght@700;800;900&family=Arimo:wght@400;700&display=swap">
<style>
  :root {
    --sky-top: #1e9ee0;
    --sky-mid: #35b1ea;
    --sky-low: #5cc4f0;
    --sun-yellow: #fff200;
    --white: #ffffff;
    --ink-blue: #1b8fd2;
    --ink-navy: #0d4f86;
    --leaf-top: #4fae35;
    --leaf-low: #0e5a26;
    --page-bg: #d9d9d9;
  }
  * { margin: 0; padding: 0; box-sizing: border-box; }
  html, body { width: 1033px; height: 1200px; overflow: hidden; }
  body {
    background: var(--page-bg);
    font-family: "Arimo", Arial, sans-serif;
  }
  .ad {
    position: absolute;
    left: 58px; top: 0;
    width: 917px; height: 1200px;
    background: linear-gradient(180deg, var(--sky-top) 0%, var(--sky-mid) 55%, var(--sky-low) 80%);
    overflow: hidden;
  }
  .dotted-frame { position: absolute; left: 0; top: 0; }
  .headline {
    position: absolute; left: 0; top: 46px; width: 917px;
    text-align: center; white-space: nowrap;
  }
  .headline h1 {
    font-family: "Nunito", sans-serif; font-weight: 900;
    color: var(--sun-yellow); font-size: 39px; line-height: 48px;
    letter-spacing: -0.3px;
    text-shadow: 0 2px 4px rgba(0,0,0,0.25);
  }
  .headline h2 {
    font-family: "Arimo", Arial, sans-serif; font-weight: 700;
    color: var(--white); font-size: 29px; line-height: 40px;
    margin-top: 2px;
    text-shadow: 0 2px 3px rgba(0,0,0,0.25);
  }
  .questions {
    position: absolute; left: 65px; top: 148px; width: 820px;
    list-style: none; white-space: nowrap;
    color: var(--sun-yellow); font-weight: 700; font-size: 18px; line-height: 23.8px;
  }
  .intro {
    position: absolute; left: 65px; top: 278px; width: 820px;
    white-space: nowrap;
    color: var(--white); font-weight: 700; font-size: 18px; line-height: 23.8px;
  }
  .faces {
    position: absolute; left: 65px; top: 392px; width: 800px; height: 233px;
    background: var(--white);
    display: flex; justify-content: space-between; padding: 14px;
  }
  .faces .portrait { width: 181px; height: 205px; }
  .portrait--a { background: linear-gradient(160deg, #6b4a34, #c79a7e 60%, #2c3b5a); }
  .portrait--b { background: linear-gradient(160deg, #d8d8d8, #c9a08a 55%, #3f7fb5); }
  .portrait--c { background: linear-gradient(160deg, #3a2a22, #caa088 55%, #f0f0f0); }
  .portrait--d { background: linear-gradient(160deg, #6a4a2c, #d2a585 55%, #e8e8e8); }
  .why-title {
    position: absolute; left: 63px; top: 636px;
    font-family: "Nunito", sans-serif; font-weight: 900;
    color: var(--white); font-size: 56px; line-height: 60px; letter-spacing: 0.5px;
    z-index: 2;
  }
  .benefits {
    position: absolute; left: 0; top: 687px; width: 917px; height: 169px;
    background: var(--white);
    z-index: 1;
  }
  .benefit {
    position: absolute; top: 12px; width: 196px;
    color: var(--ink-blue); font-size: 14px; line-height: 18.6px;
  }
  .benefit strong { color: var(--ink-navy); }
  .benefit--1 { left: 65px; }
  .benefit--2 { left: 269px; }
  .benefit--3 { left: 473px; }
  .benefit--4 { left: 678px; }
  .reassure {
    position: absolute; left: 65px; top: 874px; width: 820px; color: var(--white);
    white-space: nowrap;
  }
  .reassure h3 {
    font-family: "Nunito", sans-serif; font-weight: 800;
    font-size: 21px; line-height: 28px;
  }
  .reassure p { font-size: 13.5px; line-height: 17px; margin-top: 6px; }
  .plane { position: absolute; left: 785px; top: 918px; }
  .contact {
    position: absolute; left: 0; top: 979px; width: 917px; height: 221px;
    background: linear-gradient(180deg, var(--leaf-top) 0%, #2a8a30 40%, var(--leaf-low) 100%);
    color: var(--white);
  }
  .call {
    position: absolute; left: 0; width: 917px; top: 14px; text-align: center;
    font-family: "Nunito", sans-serif; font-weight: 800; white-space: nowrap;
    color: var(--sun-yellow); font-size: 23px; line-height: 38px;
    text-shadow: 0 2px 3px rgba(0,0,0,0.3);
  }
  .call .phone { font-size: 33px; vertical-align: -2px; }
  .email {
    position: absolute; left: 0; width: 917px; top: 58px; text-align: center;
    font-family: "Nunito", sans-serif; font-weight: 800;
    color: var(--sun-yellow); font-size: 18px; line-height: 24px;
  }
  .brand {
    position: absolute; top: 108px;
    display: flex; align-items: center; gap: 12px; white-space: nowrap;
    font-family: "Arimo", Arial, sans-serif; font-weight: 700;
    color: var(--white); font-size: 23px; line-height: 28px;
  }
  .brand--left { left: 72px; }
  .brand--right { left: 540px; }
  .brand-dot {
    width: 32px; height: 32px; border-radius: 50%;
    background: var(--white); flex: none;
  }
  .ampersand {
    position: absolute; left: 436px; top: 96px;
    font-family: "Nunito", sans-serif; font-weight: 900;
    font-size: 58px; line-height: 64px; color: rgba(140, 200, 120, 0.55);
  }
  .visit {
    position: absolute; top: 184px;
    font-weight: 700; font-size: 13.5px; white-space: nowrap;
  }
  .visit--left { left: 122px; }
  .visit--right { left: 578px; }
</style>
</head>
<body>
<main class="ad">
  <svg class="dotted-frame" width="917" height="979" viewBox="0 0 917 979" aria-hidden="true">
    <rect x="37" y="19" width="862" height="949" rx="40" ry="40"
          fill="none" stroke="#ffffff" stroke-width="3" stroke-linecap="round"
          stroke-dasharray="0.1 8" opacity="0.9"/>
  </svg>

  <header class="headline">
    <h1>Fly-in Fly-out Dental Transformations</h1>
    <h2>True Care, Advanced Expertise, Minimal Visits</h2>
  </header>

  <ul class="questions">
    <li>Are you embarrassed to smile?</li>
    <li>Do you have complex dental problems and don't know where to start?</li>
    <li>Do you suffer from fear of the dentist or just can't find the right one?</li>
    <li>No time for endless appointments?</li>
    <li>Do you wish you could just sleep your way to a healthy and attractive smile?</li>
  </ul>

  <p class="intro">If the answer is yes to any of these questions, you are certainly not alone!<br>
  In our specialized Sleep Dentistry Centre, our renowned team provides<br>
  gentle, compassionate, advanced and extensive treatments often in the<br>
  comfort of a relaxing sleep (IV Sedation).</p>

  <section class="faces">
    <div class="portrait portrait--a" role="img" aria-label="Portrait of a smiling young woman with long brown hair"></div>
    <div class="portrait portrait--b" role="img" aria-label="Portrait of a smiling grey-haired older man"></div>
    <div class="portrait portrait--c" role="img" aria-label="Portrait of a smiling woman with dark hair"></div>
    <div class="portrait portrait--d" role="img" aria-label="Portrait of a smiling young man"></div>
  </section>

  <h2 class="why-title">WHY US?</h2>
  <section class="benefits">
    <p class="benefit benefit--1">We take the time to<br>understand your needs<br>so you can make the best<br>decisions for your health.<br>You are looked after by a<br>friendly, highly qualified<br>expert team in relaxed and<br>comfortable surroundings.</p>
    <p class="benefit benefit--2">Our unique, time-saving<br>approach means our<br>patients often have<br>advanced treatments<br>that would normally take<br>months in minimal visits -<br>perfect for the Fly-in,<br>Fly-out patient.</p>
    <p class="benefit benefit--3">We offer a full range<br>of dental treatments<br>including dental implant<br>surgeries and cosmetic<br>rehabilitations all in-house.</p>
    <p class="benefit benefit--4">Our approach with Sleep<br>Dentistry means Pain-<br>Free, anxiety free, memory<br>free procedures. <strong>Just<br>excellent results and life<br>changing treatments.</strong></p>
  </section>

  <section class="reassure">
    <h3>Sound too good to be true? It's just what we do for our patients every day.</h3>
    <p>Our patients come from all over Western Australia to take advantage of this unique and personalized service.<br>
    We invite you to let us care for you as well.</p>
  </section>

  <svg class="plane" width="90" height="50" viewBox="0 0 90 50" aria-hidden="true">
    <path d="M4 40 L30 30 L18 12 L26 12 L46 27 L74 17 Q86 13 86 19 Q85 23 76 26 L48 36 L40 48 L33 48 L36 38 L10 46 Z"
          fill="none" stroke="#ffffff" stroke-width="2" stroke-linejoin="round" opacity="0.9"/>
  </svg>

  <footer class="contact">
    <p class="call">Call our friendly team in Harbourside today • <span class="phone">(08) 9460 5172</span></p>
    <p class="email">or email info@calmharbordentalcare.com</p>

    <div class="brand brand--left"><span class="brand-dot"></span>Calm Harbor Dental Care</div>
    <span class="ampersand">&amp;</span>
    <div class="brand brand--right"><span class="brand-dot"></span>Willowbank Dental Clinic</div>

    <p class="visit visit--left">Visit calmharbordentalcare.com</p>
    <p class="visit visit--right">Visit willowbankdentalclinic.com.au</p>
  </footer>
</main>
</body>
</html>
```